Thornwell Building Company - advertisement poster

I am looking to print some canvas signs to advertise my general contracting company, Thornwell Building Company. The sign will measure 6' long x 3' high so the size should match that ratio. I already have a logo icon, which is the Letter 'A' and some trees that I would like to incorporate, see attached. I would also like the to have the following information listed:
1) phone number: 472-318-6095
2) email: thornwellbuildingcompany@mailvistra.net
3) website: thornwellbuildingcompany.com
4) Lic#5386204
5) I want to use this text: "BUILD WITH THE T-CREW!"

The ad should be relatively simple and clean. Black and Green are my company colors. I am open to creative ideas!

Target Market(s)

People looking to renovate their homes

Industry/Entity Type

Construction

Colors
59FF00
82FF00
B8FF75
E3FFCB
F4FFEA

Requirements
Must have
• Must have my company logo
Should not have
• No photos or complex graphics

```html
<!DOCTYPE html>
<html lang="en">
<head>
<meta charset="UTF-8">
<title>Thornwell Building Company – Canvas Sign</title>
<link rel="stylesheet" href="https://fonts.googleapis.com/css2?family=Montserrat:wght@500;600;700;800&display=swap">
<style>
  :root {
    --ink: #231f20;
    --leaf: #6cb245;
    --paper: #ffffff;
  }
  * { margin: 0; padding: 0; box-sizing: border-box; }
  html, body {
    width: 1200px;
    height: 1200px;
    overflow: hidden;
    background: var(--paper);
    font-family: "Montserrat", Arial, sans-serif;
  }
  .sign {
    position: absolute;
    left: 88px;
    top: 343px;
    width: 1024px;
    height: 513px;
    background: var(--ink);
    overflow: hidden;
  }
  .brand {
    position: absolute;
    left: 70px;
    top: 112px;
    width: 340px;
    display: flex;
    flex-direction: column;
    align-items: center;
    gap: 14px;
    color: var(--paper);
    font-weight: 700;
    text-align: center;
  }
  .brand-mark {
    width: 90px;
    height: 90px;
    background: var(--leaf);
  }
  .brand-name {
    font-size: 44px;
    line-height: 1;
    letter-spacing: 1px;
  }
  .brand-sub {
    font-size: 19px;
    letter-spacing: 6px;
    line-height: 1;
    color: var(--leaf);
  }
  .headline {
    position: absolute;
    left: 447px;
    top: 68px;
    color: var(--paper);
    font-weight: 800;
    font-size: 76px;
    line-height: 78px;
    letter-spacing: -0.5px;
    text-transform: uppercase;
  }
  .phone {
    position: absolute;
    left: 447px;
    top: 286px;
    display: flex;
    align-items: center;
    gap: 14px;
    color: var(--leaf);
    font-weight: 800;
    font-size: 68px;
    line-height: 1;
  }
  .phone svg { width: 54px; height: 54px; }
  .email {
    position: absolute;
    left: 447px;
    top: 360px;
    display: flex;
    align-items: center;
    gap: 10px;
    color: var(--paper);
    font-weight: 700;
    font-size: 21px;
    line-height: 1;
  }
  .email svg { width: 21px; height: 15px; }
  .footer-band {
    position: absolute;
    left: 0;
    top: 422px;
    width: 1024px;
    height: 91px;
  }
  .licence {
    position: absolute;
    left: 41px;
    top: 440px;
    color: var(--paper);
    font-weight: 600;
    font-size: 28px;
    line-height: 56px;
  }
  .website {
    position: absolute;
    left: 334px;
    top: 440px;
    color: var(--paper);
    font-weight: 700;
    font-size: 38px;
    line-height: 56px;
    letter-spacing: -0.5px;
    white-space: nowrap;
  }
</style>
</head>
<body>
  <main class="sign">
    <div class="brand">
      <div class="brand-mark"></div>
      <div class="brand-name">THORNWELL</div>
      <div class="brand-sub">BUILDING COMPANY</div>
    </div>

    <h1 class="headline">Build with<br>the T-Crew!</h1>

    <div class="phone">
      <svg viewBox="0 0 54 54" aria-hidden="true">
        <path fill="var(--leaf)" d="M8 4c3-2 6-1 7 2l4 10c1 3 0 5-2 6l-3 2c3 7 9 13 16 16l2-3c1-2 3-3 6-2l10 4c3 1 4 4 2 7l-3 4c-2 3-6 4-10 3C23 48 6 31 3 18 2 13 3 9 6 6z"/>
        <path fill="none" stroke="var(--leaf)" stroke-width="3.5" stroke-linecap="round" d="M30 14c5 1 9 5 10 10M31 5c10 1 17 9 18 19"/>
      </svg>
      <span>472-318-6095</span>
    </div>

    <div class="email">
      <svg viewBox="0 0 21 15" aria-hidden="true">
        <rect x="0" y="0" width="21" height="15" rx="1.5" fill="var(--paper)"/>
        <path d="M1.5 2l9 7 9-7M1.5 13.5l6-5M19.5 13.5l-6-5" fill="none" stroke="var(--ink)" stroke-width="1.2"/>
      </svg>
      <span>thornwellbuildingcompany@mailvistra.net</span>
    </div>

    <svg class="footer-band" viewBox="0 0 1024 91" aria-hidden="true">
      <polygon points="306,0 1024,0 1024,91 272,91" fill="var(--leaf)"/>
    </svg>

    <div class="licence">Lic#5386204</div>
    <div class="website">thornwellbuildingcompany.com</div>
  </main>
</body>
</html>
```